Marnie Holloway 2014 Calendar

We need a 12 month, wall hanging Calendar design featuring the actress Marnie Holloway. It is a product for her fans and the feel of this years photographs is very otherworldly with saturated colors and the incorporation of elements such as fire, ice and water. We are looking for bold, graphic designs to support and reflect this feel. There is a very tight schedule for the completion of this calendar as it needs to go into production asap so any designers submitting concepts should have the ability and enthusiasm to dedicate the necessary time required to get this product to the printers quickly.
We have included three of the twelve photographs for you to use with a combination of vertical and horizontal images. Once the design is selected we will provide the remaining nine photos to be incorporated. These images are to be kept completely confidential please.
Thank you and we are looking forward to seeing your ideas!!
Industry/Entity Type
Product
Requirements
Must have
- Bio about Marnie Holloway, crédits for art director, photographer etc. Some negative space on cover so that it maybe autographed by actress. 12 months reflected in page design.

```html
<!DOCTYPE html>
<html lang="en">
<head>
<meta charset="utf-8">
<title>Marnie Holloway – 2014 calendar plan</title>
<link rel="stylesheet" href="https://fonts.googleapis.com/css2?family=Cabin:wght@400;500&family=Playfair+Display:wght@400&family=Lato:wght@400;700&display=swap">
<style>
  :root{
    --board:#ffffff;
    --ink:#1e1e1e;
    --page:#ffffff;
    --accent:#a3282e;
    --muted:#9a9a9a;
    --rule:#c9c9c9;
    --shadow:rgba(0,0,0,.35);
  }
  *{box-sizing:border-box;margin:0;padding:0}
  html,body{width:1200px;height:857px;overflow:hidden;background:var(--board)}
  .board{position:relative;width:1200px;height:857px;font-family:"Cabin",sans-serif;color:var(--ink)}
  .board-title{position:absolute;left:60px;top:64px;font-size:27px;font-weight:400;letter-spacing:-.2px}
  .section-title{position:absolute;left:0;width:100%;top:150px;text-align:center;font-size:25px;font-weight:400}
  .page{position:absolute;top:210px;width:280px;height:563px;background:var(--page);
        box-shadow:6px 7px 9px var(--shadow);overflow:hidden}
  .page--july{left:115px}
  .page--february{left:453px}
  .page--december{left:790px}
  .photo{position:absolute;left:0;width:100%}
  .photo--full{top:0;height:423px}
  .photo--top{top:0;height:282px}
  .photo--strip{top:360px;height:63px}
  .july-photo{background:radial-gradient(ellipse at 45% 40%,#c8702a 0%,#7a3514 40%,#2a0f06 85%)}
  .february-photo{background:linear-gradient(160deg,#3a1418 0%,#8a2027 40%,#2c3a2e 70%,#1a1a1e 100%)}
  .lantern-photo{background:radial-gradient(ellipse at 50% 60%,#f39a3a 0%,#b8521d 45%,#3a1408 100%)}
  .december-photo{background:linear-gradient(180deg,#274d6b 0%,#6a93ac 45%,#b7cbd6 75%,#dfe7ec 100%)}
  .month-name{position:absolute;left:0;width:100%;text-align:center;font-family:"Playfair Display",serif;
              font-weight:400;line-height:1;text-transform:uppercase;letter-spacing:0;
              font-size:50px;transform:scaleX(.8);transform-origin:50% 50%}
  .month-name--overlay{color:#fff;text-shadow:0 2px 6px rgba(0,0,0,.55)}
  .page--july .month-name{top:366px}
  .page--february .month-name{top:297px;color:var(--accent)}
  .page--december .month-name{top:296px}
  .grid{position:absolute;left:27px;top:440px;width:226px;border-collapse:collapse;
        font-family:"Lato",sans-serif;font-size:6.5px;color:var(--accent);text-align:center}
  .grid th{font-weight:700;height:13px;border-bottom:1px solid var(--rule);font-size:5.5px;letter-spacing:.3px}
  .grid td{height:18px}
  .page--december .grid{color:var(--muted)}
  .footer{position:absolute;left:0;width:100%;top:543px;text-align:center;font-family:"Lato",sans-serif;
          font-size:4.5px;letter-spacing:.5px;color:#555;text-transform:uppercase}
</style>
</head>
<body>
<main class="board">
  <h1 class="board-title">Marnie Holloway - 2014 calendar plan</h1>
  <h2 class="section-title">Month pages examples</h2>

  <article class="page page--july">
    <div class="photo photo--full july-photo" role="img" aria-label="Photograph area for the July image"></div>
    <div class="month-name month-name--overlay">July</div>
    <table class="grid">
      <tr><th>MON</th><th>TUE</th><th>WED</th><th>THU</th><th>FRI</th><th>SAT</th><th>SUN</th></tr>
      <tr><td></td><td>1</td><td>2</td><td>3</td><td>4</td><td>5</td><td>6</td></tr>
      <tr><td>7</td><td>8</td><td>9</td><td>10</td><td>11</td><td>12</td><td>13</td></tr>
      <tr><td>14</td><td>15</td><td>16</td><td>17</td><td>18</td><td>19</td><td>20</td></tr>
      <tr><td>21</td><td>22</td><td>23</td><td>24</td><td>25</td><td>26</td><td>27</td></tr>
      <tr><td>28</td><td>29</td><td>30</td><td>31</td><td></td><td></td><td></td></tr>
    </table>
    <div class="footer">Marnie Holloway 2014 calendar</div>
  </article>

  <article class="page page--february">
    <div class="photo photo--top february-photo" role="img" aria-label="Photograph area for the February image"></div>
    <div class="month-name">February</div>
    <div class="photo photo--strip lantern-photo" role="img" aria-label="Secondary photograph strip for February"></div>
    <table class="grid">
      <tr><th>MON</th><th>TUE</th><th>WED</th><th>THU</th><th>FRI</th><th>SAT</th><th>SUN</th></tr>
      <tr><td></td><td></td><td></td><td></td><td></td><td>1</td><td>2</td></tr>
      <tr><td>3</td><td>4</td><td>5</td><td>6</td><td>7</td><td>8</td><td>9</td></tr>
      <tr><td>10</td><td>11</td><td>12</td><td>13</td><td>14</td><td>15</td><td>16</td></tr>
      <tr><td>17</td><td>18</td><td>19</td><td>20</td><td>21</td><td>22</td><td>23</td></tr>
      <tr><td>24</td><td>25</td><td>26</td><td>27</td><td>28</td><td></td><td></td></tr>
    </table>
    <div class="footer">Marnie Holloway 2014 calendar</div>
  </article>

  <article class="page page--december">
    <div class="photo photo--full december-photo" role="img" aria-label="Photograph area for the December image"></div>
    <div class="month-name month-name--overlay">December</div>
    <table class="grid">
      <tr><th>MON</th><th>TUE</th><th>WED</th><th>THU</th><th>FRI</th><th>SAT</th><th>SUN</th></tr>
      <tr><td>1</td><td>2</td><td>3</td><td>4</td><td>5</td><td>6</td><td>7</td></tr>
      <tr><td>8</td><td>9</td><td>10</td><td>11</td><td>12</td><td>13</td><td>14</td></tr>
      <tr><td>15</td><td>16</td><td>17</td><td>18</td><td>19</td><td>20</td><td>21</td></tr>
      <tr><td>22</td><td>23</td><td>24</td><td>25</td><td>26</td><td>27</td><td>28</td></tr>
      <tr><td>29</td><td>30</td><td>31</td><td></td><td></td><td></td><td></td></tr>
    </table>
    <div class="footer">Marnie Holloway 2014 calendar</div>
  </article>
</main>
</body>
</html>
```